I need a business card design for a new company that will be doing consulting work around issues of cultural competency, and diversity and inclusion. I would like the design to be crisp and clear with bold but conservative colors and incorporate shades of blue

Target Market(s)

Small businesses, schools, non-profits

Industry/Entity Type

Consulting

Font styles to use
Serif
Sans Serif

Colors
0c5ba6
6b449b
3276b5
0292cd

Requirements
Must have
• A Morrow Venture (name of company)
• Lemlem Tavish
• CEO
• lemlem@amorrowventure.com
• (215)483-2756

```html
<!DOCTYPE html>
<html lang="en">
<head>
<meta charset="utf-8">
<title>Lemlem Tavish — Business Card</title>
<link rel="stylesheet" href="https://fonts.googleapis.com/css2?family=Noto+Sans+Mono:wght@400;600&family=Open+Sans:wght@400&display=swap">
<style>
  :root {
    --canvas-bg: #e9e7e4;
    --card-blue: #4fabd6;
    --card-text: #ffffff;
  }
  html, body {
    margin: 0;
    padding: 0;
    width: 1200px;
    height: 1200px;
    overflow: hidden;
    background: var(--canvas-bg);
  }
  .canvas {
    position: relative;
    width: 1200px;
    height: 1200px;
  }
  .business-card {
    position: absolute;
    left: 60px;
    top: 250px;
    width: 1080px;
    height: 700px;
    background: var(--card-blue);
    color: var(--card-text);
    overflow: hidden;
  }
  .business-card > * {
    position: absolute;
    margin: 0;
    line-height: 1;
    white-space: nowrap;
  }
  .person-name {
    left: 4px;
    top: 240px;
    font-family: "Noto Sans Mono", monospace;
    font-size: 134px;
    font-weight: 400;
    letter-spacing: 2px;
  }
  .person-name .surname {
    font-weight: 600;
  }
  .person-title {
    right: 28px;
    top: 386px;
    font-family: "Open Sans", sans-serif;
    font-size: 40px;
  }
  .contact-email,
  .contact-phone {
    left: 22px;
    font-family: "Noto Sans Mono", monospace;
    font-size: 44px;
    letter-spacing: 2px;
  }
  .contact-email { top: 432px; }
  .contact-phone { top: 497px; }
  .company-name {
    right: 40px;
    top: 604px;
    font-family: "Noto Sans Mono", monospace;
    font-size: 44px;
    letter-spacing: 6px;
  }
</style>
</head>
<body>
  <main class="canvas">
    <section class="business-card">
      <h1 class="person-name">Lemlem <span class="surname">Tavish</span></h1>
      <p class="person-title">CEO</p>
      <p class="contact-email">lemlem@amorrowventure.com</p>
      <p class="contact-phone">(215)483-2756</p>
      <p class="company-name">A Morrow Venture</p>
    </section>
  </main>
</body>
</html>
```